もみほぐし、マッサージ店の看板デザイン(二種類)を依頼させて頂きます。

1.店舗に設置するヨコ看板   横350cm×縦75cm
2.店外に設置するスタンド看板 横42cm×縦113cm
(設置位置は添付画像をご覧ください、また参考程度に添付エクセルをご覧くださいませ)

場所は、県では一番賑わっているアーケード内の繁華街となります。
誰でもお越しいただける「安心感、癒し、やわらかさ」と
街中ですので「多少の洗練」を希望いたします。
一目で「マッサージ、指圧、もみほぐし」と直感できると嬉しいです。

店内は明るいライムグリーンを基調としておりますが、
ブランド力はありませんので、目につきやすい配色で人目を引ければと思います。

準備中ではございますが、店内の画像も添付いたしましたのでご覧ください。

会社名  フワリK 桜木通り店
電話番号 096-555-0172
営業時間 朝10時から翌朝5時

・「全身ほぐしコース 60分 税込 2980円」

・価格テーブル(添付エクセルデータをご覧ください)

・「深夜0時以降は、プラス100円いただきます」

・エレベータをのぼって2階にあるため「2F」

・ロゴ等はなにぶん開業前ですので、特にございません。

文言で強調していただきたいポイントは
「全身ほぐしコース60分2980円」の割安感と
2回にあるため「2F」というところです。
明るめのライムグリーン、強調する意味での赤など。他にも良い案をご提案下さい。
なにぶん初めての依頼ですので、いたらない部分もあるかと思いますが、誠実に対応させていただきますので、どうぞよろしくお願いいたします。
すみません。
記載項目の記述は、スタンド看板だけを念頭に置いて書いてしまいました。

ヨコ看板に最低限載せていただきたい記載文言は

・店舗名 フワリK 桜木通店
・全身(※もみ)ほぐし(※コース)60分 税込 2980円
・電話番号 096-555-0172

の3つとなります(※は必須ではございません)
よろしくお願いいたします。
時間も差し迫ったところで、申し訳ございませんが、
強く希望させていただきたいポイントと
変更内容を追記いたします。

【希望】
1)上部のヨコ看板についてですが
店名等より「全身もみほぐし 60分 2980円(税込)」
という文言を、より大きく前面に押し出していただきたいです。
(税込)もお願いいたします。

2)下のスタンド看板についてです。
価格テーブルを必ず載せて欲しいです。
(もみほぐし)(足つぼ)(もみほぐし&足つぼハーフ)(眼精疲労コース)
以上の4種類です。

3)写真についての希望です。
当店ではお客様任意の動きやすい服装か、ジャージをお貸しして
その上からタオルを載せて施術するという形をとりますので
素材がございましたら、着衣の画像をお願いいたします。
これはあくまで希望で必須ではありません。

4)店名について。
「フワリ」はカタカナ。「M」はアルファベットをお願いいたします。

【変更】
眼精疲労コースの時間と料金を変更いたします。
「15分1080円」となります。
価格テーブルのエクセルファイルをアップロードいたしますのでご覧ください。

以上よろしくお願い申し上げます。
こちらの説明不足でご迷惑をおかけします。
(マッサージ)という言葉が法律に抵触する可能性も考えられます。
(マッサージ)という単語は看板では使わない方向で考えておりますので
よろしくお願いいたします。
募集終了後、当選候補者様をお選びし修正依頼を
お送り致しますが少々急いでおりますので納品を
明日、11日15時までにお願いしたいと考えております。
もし修正依頼を受け取られた候補者様のスケジュールが
合わず、11日15時に間に合わないと判断された場合は
即座にお断りのご連絡を頂けましたら幸いです。
こちらの勝手な都合を押しつけるようで誠に恐縮ですが
よろしく申し上げます。

配色、デザインが最も洗練されていると感じました。
一目で気に入りました。
親指を鳥の目に見立てた「M」のロゴマークも素晴らしいと思いました。

こちらの度重なる修正依頼にも迅速に、誠実に対応して頂きました。

予想を超えるご応募をいただき誠に感謝しております。
たくさん良いデザインがありましたので一つお選びするのは
大変心苦しかったです。

皆さまありがとうございました。

```html
<!DOCTYPE html>
<html lang="ja">
<head>
<meta charset="utf-8">
<title>フワリK 桜木通店 スタンド看板</title>
<link href="https://fonts.googleapis.com/css2?family=Noto+Sans+JP:wght@500;700;900&display=swap" rel="stylesheet">
<style>
:root{
  --yellow:#f6c21c;
  --red:#e5141e;
  --dark-red:#a3161c;
  --blue:#1f6fb6;
  --green:#3a9a34;
  --orange:#ea6a12;
  --ink:#111;
  --white:#fff;
}
*{margin:0;padding:0;box-sizing:border-box}
html,body{width:1200px;height:3208px;overflow:hidden;background:var(--yellow)}
body{font-family:"Noto Sans JP",sans-serif;color:var(--ink);position:relative}
.photo{position:absolute;left:48px;top:32px;width:1104px;height:728px;
  background:linear-gradient(135deg,#f4f4f2 0%,#e8d4c4 40%,#c99a80 60%,#2a2a2a 85%,#111 100%)}
.floor-badge{position:absolute;left:912px;top:400px;width:240px;height:360px;background:#111;border:6px solid var(--white);
  display:flex;flex-direction:column;align-items:center;justify-content:center;gap:20px;color:var(--white)}
.floor-badge .floor{font-size:118px;font-weight:900;line-height:1;display:flex;align-items:center;gap:8px}
.headline{position:absolute;left:0;width:1200px;text-align:center;font-weight:900;line-height:1}
.headline.course{top:850px;font-size:124px;letter-spacing:2px}
.headline.price{top:1010px;color:var(--red);font-size:158px;letter-spacing:-2px}
.price small{font-size:40px;vertical-align:top;position:relative;top:12px;letter-spacing:0}
.price .unit{font-size:118px}
.price-table{position:absolute;left:88px;top:1272px;width:1032px;border-collapse:collapse;background:var(--white);table-layout:fixed}
.price-table th,.price-table td{border:4px solid #333;height:96px;font-weight:900;font-size:50px;text-align:right;padding-right:22px;position:relative}
.price-table th{height:120px;color:var(--white);text-align:center;padding:0;font-size:38px;line-height:1.15}
.price-table th.small{font-size:28px}
.price-table td.min{text-align:center;padding:0;font-size:30px;font-weight:700}
.col-min{background:var(--dark-red)}
.col-momi{background:var(--red)}
.col-foot{background:var(--blue)}
.col-half{background:var(--green)}
.col-eye{background:var(--orange)}
.t-red{color:var(--red)} .t-blue{color:var(--blue)} .t-green{color:var(--green)} .t-orange{color:var(--orange)}
.empty svg{position:absolute;inset:0;width:100%;height:100%}
.fees{position:absolute;left:88px;top:1990px;font-size:52px;font-weight:900;white-space:nowrap}
.fees em{font-style:normal;color:var(--red)}
.notes{position:absolute;left:88px;top:2064px;font-size:30px;font-weight:700;color:var(--red);line-height:1.35}
.notes p:last-child{padding-left:60px}
.contact{position:absolute;left:88px;display:flex;align-items:center;gap:26px;font-weight:900}
.contact.tel{top:2250px;font-size:100px}
.contact.hours{top:2455px;font-size:78px}
.icon-box{width:120px;height:120px;background:var(--orange);display:flex;align-items:center;justify-content:center}
.hours .icon-box{width:100px;height:120px;color:var(--white);font-size:36px;line-height:1.1;text-align:center;flex-direction:column}
.shop-band{position:absolute;left:0;top:2672px;width:1200px;height:536px;background:var(--orange);color:var(--white);text-align:center;font-weight:900}
.shop-band .name{margin-top:118px;font-size:118px;letter-spacing:6px;line-height:1}
.shop-band .branch{margin-top:46px;font-size:74px;letter-spacing:26px;line-height:1}
</style>
</head>
<body>
<div class="photo" role="img" aria-label="施術者が客の手を指圧でほぐしている写真"></div>
<div class="floor-badge">
  <div class="floor">2F<svg width="56" height="100" viewBox="0 0 56 100"><path d="M28 4 L28 96 M6 28 L28 4 L50 28" stroke="#fff" stroke-width="9" fill="none"/></svg></div>
  <svg width="180" height="150" viewBox="0 0 180 150" fill="none" stroke="#fff" stroke-width="6">
    <rect x="4" y="4" width="172" height="142"/>
    <g fill="#fff" stroke="none">
      <circle cx="45" cy="40" r="13"/><rect x="30" y="58" width="30" height="70" rx="6"/>
      <circle cx="90" cy="40" r="13"/><rect x="75" y="58" width="30" height="70" rx="6"/>
      <circle cx="135" cy="40" r="13"/><rect x="120" y="58" width="30" height="70" rx="6"/>
    </g>
  </svg>
</div>

<h1 class="headline course">全身もみほぐし</h1>
<p class="headline price">60<span class="unit">分</span>2,980<span class="unit">円</span><small>(税込)</small></p>

<table class="price-table">
  <colgroup><col style="width:80px"><col style="width:240px"><col style="width:240px"><col style="width:240px"><col style="width:232px"></colgroup>
  <tr>
    <th class="col-min">分</th><th class="col-momi">もみほぐし</th><th class="col-foot">足つぼ</th>
    <th class="col-half small">もみほぐし&amp;<br>足つぼハーフ</th><th class="col-eye small">眼精疲労<br>コース</th>
  </tr>
  <tr><td class="min">15</td><td class="t-red">980</td>
    <td class="empty"><svg viewBox="0 0 10 10" preserveAspectRatio="none"><line x1="0" y1="10" x2="10" y2="0" stroke="#333" stroke-width=".15"/></svg></td>
    <td class="empty"><svg viewBox="0 0 10 10" preserveAspectRatio="none"><line x1="0" y1="10" x2="10" y2="0" stroke="#333" stroke-width=".15"/></svg></td>
    <td class="t-orange">1,080</td></tr>
  <tr><td class="min">30</td><td class="t-red">1,780</td><td class="t-blue">2,280</td>
    <td class="empty"><svg viewBox="0 0 10 10" preserveAspectRatio="none"><line x1="0" y1="10" x2="10" y2="0" stroke="#333" stroke-width=".15"/></svg></td>
    <td class="empty"><svg viewBox="0 0 10 10" preserveAspectRatio="none"><line x1="0" y1="10" x2="10" y2="0" stroke="#333" stroke-width=".15"/></svg></td></tr>
  <tr><td class="min">45</td><td class="t-red">2,480</td><td class="t-blue">2,980</td>
    <td class="empty"><svg viewBox="0 0 10 10" preserveAspectRatio="none"><line x1="0" y1="10" x2="10" y2="0" stroke="#333" stroke-width=".15"/></svg></td>
    <td class="empty"><svg viewBox="0 0 10 10" preserveAspectRatio="none"><line x1="0" y1="10" x2="10" y2="0" stroke="#333" stroke-width=".15"/></svg></td></tr>
  <tr><td class="min">60</td><td class="t-red">2,980</td><td class="t-blue">3,580</td><td class="t-green">3,380</td>
    <td class="empty"><svg viewBox="0 0 10 10" preserveAspectRatio="none"><line x1="0" y1="10" x2="10" y2="0" stroke="#333" stroke-width=".15"/></svg></td></tr>
  <tr><td class="min">90</td><td class="t-red">4,680</td><td class="t-blue">5,380</td><td class="t-green">4,980</td>
    <td class="empty"><svg viewBox="0 0 10 10" preserveAspectRatio="none"><line x1="0" y1="10" x2="10" y2="0" stroke="#333" stroke-width=".15"/></svg></td></tr>
  <tr><td class="min">120</td><td class="t-red">6,280</td><td class="t-blue">7,180</td><td class="t-green">6,680</td>
    <td class="empty"><svg viewBox="0 0 10 10" preserveAspectRatio="none"><line x1="0" y1="10" x2="10" y2="0" stroke="#333" stroke-width=".15"/></svg></td></tr>
</table>

<p class="fees">個人指名料 <em>¥300</em>　男女指名料 <em>¥100</em></p>
<div class="notes">
  <p>※表示価格はすべて税込価格です。</p>
  <p>深夜12時以降は、合計金額よりプラス¥100を頂きます。</p>
</div>

<div class="contact tel">
  <span class="icon-box"><svg width="76" height="76" viewBox="0 0 24 24"><path fill="#fff" d="M6.6 10.8a15.2 15.2 0 0 0 6.6 6.6l2.2-2.2c.3-.3.7-.4 1-.2 1.1.4 2.3.6 3.6.6.6 0 1 .4 1 1V20c0 .6-.4 1-1 1A17 17 0 0 1 3 4c0-.6.4-1 1-1h3.5c.6 0 1 .4 1 1 0 1.3.2 2.5.6 3.6.1.3 0 .7-.2 1z"/></svg></span>
  <span>096-555-0172</span>
</div>
<div class="contact hours">
  <span class="icon-box">営業<br>時間</span>
  <span>朝10時～翌朝5時</span>
</div>

<footer class="shop-band">
  <p class="name">フワリK</p>
  <p class="branch">桜木通店</p>
</footer>
</body>
</html>
```